Endocrinologist needs new stationery

I have a logo from ArtHiveLab and now need stationery with the new logo.

Address: Suite 4, 238 Kestrel Lane, Larkfield, VIC 3284
Phone: 03 9412 7053
Fax: 03 9412 7055
Website: www.drmelvaparkson.com.au
Email: admin@drmelvaparkson.com.au

```html
<!DOCTYPE html>
<html lang="en">
<head>
<meta charset="utf-8">
<title>Dr Melva Parkson – Stationery Set</title>
<link href="https://fonts.googleapis.com/css2?family=Open+Sans:wght@400;600&family=Tinos&display=swap" rel="stylesheet">
<style>
:root{
  --bg:#1d1f20;
  --plum:#76505f;
  --blue:#2c6c9c;
  --paper:#ffffff;
  --ink:#555a60;
  --rule:#8a8f94;
  --label:#ffffff;
  --card-ink:#e9dde3;
  --card-rule:#c8b3bd;
}
*{box-sizing:border-box;margin:0;padding:0}
html,body{width:696px;height:1200px;overflow:hidden;background:var(--bg)}
.canvas{position:relative;width:696px;height:1200px;font-family:"Tinos",serif;color:var(--ink)}
.label{position:absolute;font-family:"Open Sans",sans-serif;font-size:12px;color:var(--label)}
.sheet{position:absolute;background:var(--paper);overflow:hidden}
.logo{position:absolute;left:9px;right:9px;display:flex;align-items:flex-end;gap:4px}
.logo .name{font-family:"Tinos",serif;color:var(--blue);white-space:nowrap;line-height:1}
.logo .rule{flex:1;height:0;border-top:.6px solid var(--rule);margin-bottom:2px}
.contacts{position:absolute;left:9px;list-style:none;font-size:5px;line-height:1.6}
.contacts li{display:flex;align-items:center;gap:2px;white-space:nowrap}
.ic{width:4px;height:4px;fill:var(--blue);stroke:var(--blue)}
.address{position:absolute;right:9px;font-size:5px;line-height:1.25;text-align:right;white-space:nowrap}
.band{position:absolute;left:0;bottom:0;width:100%;height:7px;display:block}
.lines{position:absolute;left:8px;right:8px;top:66px;list-style:none}
.lines li{height:10.5px;border-bottom:.5px solid #b8bcc0}
.compliments{position:absolute;left:9px;top:46px;font-size:9.5px;color:var(--plum)}
.rx-fields{position:absolute;left:9px;right:9px;top:36px;font-size:4.6px;color:var(--blue);padding-bottom:4px;border-bottom:.6px solid var(--rule);white-space:nowrap;overflow:hidden}
.rx-divider{position:absolute;left:65px;top:53px;height:250px;border-left:.6px solid var(--rule)}
.card-front{background:var(--plum)}
.card-front .logo{left:62px;right:26px;top:52px}
.card-front .name{color:var(--card-ink);font-size:15px}
.card-front .rule{border-top-color:var(--card-rule)}
</style>
</head>
<body>
<svg width="0" height="0" style="position:absolute" aria-hidden="true">
  <symbol id="i-phone" viewBox="0 0 10 10"><path d="M2 1h2l1 2-1 1a5 5 0 0 0 2 2l1-1 2 1v2a1 1 0 0 1-1 1A8 8 0 0 1 1 2a1 1 0 0 1 1-1z" stroke="none"/></symbol>
  <symbol id="i-fax" viewBox="0 0 10 10"><rect x="3" y="1" width="4" height="3" stroke="none"/><rect x="1" y="4" width="8" height="4" rx="1" stroke="none"/><rect x="3" y="7" width="4" height="2" stroke="none"/></symbol>
  <symbol id="i-mail" viewBox="0 0 10 10"><rect x="1" y="2.5" width="8" height="5.5" stroke="none"/><path d="M1 2.5l4 3 4-3" fill="none" stroke="#fff" stroke-width=".8"/></symbol>
  <symbol id="i-web" viewBox="0 0 10 10"><circle cx="5" cy="5" r="4" fill="none" stroke-width="1"/><ellipse cx="5" cy="5" rx="1.8" ry="4" fill="none" stroke-width=".8"/><path d="M1 5h8" stroke-width=".8"/></symbol>
  <symbol id="band" viewBox="0 0 100 10" preserveAspectRatio="none"><polygon points="0,0 62,0 64,10 0,10" fill="#76505f"/><polygon points="63.6,0 100,0 100,10 65.6,10" fill="#2c6c9c"/></symbol>
</svg>

<main class="canvas">

  <p class="label" style="left:56px;top:28px;font-weight:600">Business Card_3</p>
  <section class="sheet card-front" style="left:70px;top:64px;width:230px;height:132px">
    <div class="logo"><span class="name">Dr Melva Parkson</span><span class="rule"></span></div>
  </section>
  <section class="sheet" style="left:70px;top:214px;width:230px;height:132px">
    <div class="logo" style="top:30px"><span class="name" style="font-size:12px">Dr Melva Parkson</span><span class="rule"></span></div>
    <ul class="contacts" style="bottom:18px">
      <li><svg class="ic"><use href="#i-phone"/></svg>03 9412 7053</li>
      <li><svg class="ic"><use href="#i-fax"/></svg>03 9412 7055</li>
      <li><svg class="ic"><use href="#i-mail"/></svg>admin@drmelvaparkson.com.au</li>
      <li><svg class="ic"><use href="#i-web"/></svg>www.drmelvaparkson.com.au</li>
    </ul>
    <p class="address" style="bottom:22px">Suite 4, 238 Kestrel Lane<br>Larkfield, VIC 3284</p>
    <svg class="band" style="height:6px"><use href="#band"/></svg>
  </section>

  <p class="label" style="left:416px;top:23px">Note Pads_3</p>
  <section class="sheet" style="left:416px;top:47px;width:228px;height:161px">
    <div class="logo" style="top:10px"><span class="name" style="font-size:11px">Dr Melva Parkson</span><span class="rule"></span></div>
    <ul class="contacts" style="top:28px;font-size:4px">
      <li><svg class="ic"><use href="#i-phone"/></svg>03 9412 7053</li>
      <li><svg class="ic"><use href="#i-fax"/></svg>03 9412 7055</li>
      <li><svg class="ic"><use href="#i-mail"/></svg>admin@drmelvaparkson.com.au</li>
      <li><svg class="ic"><use href="#i-web"/></svg>www.drmelvaparkson.com.au</li>
    </ul>
    <p class="address" style="top:44px;right:12px;font-size:4px">Suite 4, 238 Kestrel Lane<br>Larkfield, VIC 3284</p>
    <ul class="lines"><li></li><li></li><li></li><li></li><li></li><li></li><li></li><li></li></ul>
    <svg class="band" style="height:6px"><use href="#band"/></svg>
  </section>

  <p class="label" style="left:416px;top:233px">Comp Slips_3</p>
  <section class="sheet" style="left:416px;top:259px;width:244px;height:115px">
    <div class="logo" style="top:12px"><span class="name" style="font-size:12px">Dr Melva Parkson</span><span class="rule"></span></div>
    <p class="compliments">With Compliments</p>
    <ul class="contacts" style="top:74px;font-size:4.3px">
      <li><svg class="ic"><use href="#i-phone"/></svg>03 9412 7053</li>
      <li><svg class="ic"><use href="#i-fax"/></svg>03 9412 7055</li>
      <li><svg class="ic"><use href="#i-mail"/></svg>admin@drmelvaparkson.com.au</li>
      <li><svg class="ic"><use href="#i-web"/></svg>www.drmelvaparkson.com.au</li>
    </ul>
    <p class="address" style="top:92px;font-size:4.3px">Suite 4, 238 Kestrel Lane<br>Larkfield, VIC 3284</p>
    <svg class="band" style="height:6px"><use href="#band"/></svg>
  </section>

  <p class="label" style="left:56px;top:422px">Letterhead_3</p>
  <section class="sheet" style="left:56px;top:449px;width:274px;height:355px">
    <div class="logo" style="top:12px"><span class="name" style="font-size:12px">Dr Melva Parkson</span><span class="rule"></span></div>
    <ul class="contacts" style="bottom:12px">
      <li><svg class="ic"><use href="#i-phone"/></svg>03 9412 7053</li>
      <li><svg class="ic"><use href="#i-fax"/></svg>03 9412 7055</li>
      <li><svg class="ic"><use href="#i-mail"/></svg>admin@drmelvaparkson.com.au</li>
      <li><svg class="ic"><use href="#i-web"/></svg>www.drmelvaparkson.com.au</li>
    </ul>
    <p class="address" style="bottom:16px">Suite 4, 238 Kestrel Lane<br>Larkfield, VIC 3284</p>
    <svg class="band" style="height:6px"><use href="#band"/></svg>
  </section>

  <p class="label" style="left:376px;top:422px">Prescription Pad_3</p>
  <section class="sheet" style="left:376px;top:449px;width:274px;height:355px">
    <div class="logo" style="top:12px"><span class="name" style="font-size:12px">Dr Melva Parkson</span><span class="rule"></span></div>
    <p class="rx-fields">Name ..................................................................................... Age .................... Sex .................... &nbsp; Date ...............................</p>
    <span class="rx-divider"></span>
    <ul class="contacts" style="bottom:12px">
      <li><svg class="ic"><use href="#i-phone"/></svg>03 9412 7053</li>
      <li><svg class="ic"><use href="#i-fax"/></svg>03 9412 7055</li>
      <li><svg class="ic"><use href="#i-mail"/></svg>admin@drmelvaparkson.com.au</li>
      <li><svg class="ic"><use href="#i-web"/></svg>www.drmelvaparkson.com.au</li>
    </ul>
    <p class="address" style="bottom:16px">Suite 4, 238 Kestrel Lane<br>Larkfield, VIC 3284</p>
    <svg class="band" style="height:6px"><use href="#band"/></svg>
  </section>

  <p class="label" style="left:56px;top:846px">ENV Front_3</p>
  <section class="sheet" style="left:56px;top:874px;width:282px;height:122px">
    <div class="logo" style="top:10px;right:170px;width:103px"><span class="name" style="font-size:12px">Dr Melva Parkson</span><span class="rule"></span></div>
    <p class="address" style="left:9px;right:auto;top:95px;text-align:left;font-size:4.5px">Suite 4, 238 Kestrel Lane<br>Larkfield, VIC 3284</p>
    <svg class="band" style="height:6px"><use href="#band"/></svg>
  </section>

  <p class="label" style="left:362px;top:846px">ENV Back_3</p>
  <section class="sheet" style="left:362px;top:874px;width:281px;height:122px">
    <svg width="281" height="46" viewBox="0 0 281 46" style="position:absolute;left:0;top:0" aria-hidden="true">
      <path d="M0 0H111L160 42L150 45L15 22C6 18 3 10 0 0Z" fill="var(--plum)"/>
      <path d="M113 0H281C277 12 273 20 262 24L161 41Z" fill="var(--blue)"/>
    </svg>
  </section>

  <p class="label" style="left:199px;top:1021px">Email signature_3</p>
  <section class="sheet" style="left:199px;top:1051px;width:296px;height:99px">
    <div class="logo" style="top:20px"><span class="name" style="font-size:13px">Dr Melva Parkson</span><span class="rule"></span></div>
    <ul class="contacts" style="top:50px;font-size:5.2px;line-height:1.7">
      <li><svg class="ic"><use href="#i-phone"/></svg>03 9412 7053</li>
      <li><svg class="ic"><use href="#i-fax"/></svg>03 9412 7055</li>
      <li><svg class="ic"><use href="#i-mail"/></svg>admin@drmelvaparkson.com.au</li>
      <li><svg class="ic"><use href="#i-web"/></svg>www.drmelvaparkson.com.au</li>
    </ul>
    <p class="address" style="top:70px;font-size:5.2px">Suite 4, 238 Kestrel Lane<br>Larkfield, VIC 3284</p>
    <svg class="band" style="height:11px"><use href="#band"/></svg>
  </section>

</main>
</body>
</html>
```